Pub/Bar snack and nibbles packaging

What we want:
We require professional packaging design for our jerky range.

About us and why we're here:
We're a husband and wife team from a small town who has been supplying artesian dried meats to local pubs/bars in outback Australia. Through word of mouth our volume has been growing steadily these few years. We seek someone who can assist provide a packaging range that best represents what great products my wife and I have been producing. And ultimately, a packaging that this product deserves. We have attached pictures of bar/pubs to give an idea of where our product is typically placed.

Target Market(s)

Target market:
Our customers are patrons of country motels / pubs and convenience stores. Our jerky goes particularly well with a cold beer.

Industry/Entity Type

It Professional

Requirements
Must have
• Specifics:
• Business Name: Gumridge Meats. Artisan Style.
• Product: Beef Chunks (we have 4 different flavours original, spicy, honey, pepper. The design should be easily changeable to accomodate different flavours)
• Description: Made from 100% Australian Beef
• Typography: We have attached some fonts for inspiration (e.g., lazy falcon, other alcohol brands)
• Packet Size: 110mm (w) x 170mm (l)
• We also require the back of the packaging designed as well. That information will be provided to the winning designer chosen.
Nice to have
• Design Concept:
• The design should tell a story which features an outback or bush setting. We have provided a few examples for inspiration (e.g., jackaroo walking with working dog, on a horse, swagman camping) or come up with your own. We will decide the final design based on the story that we can most related to.
Should not have
• We do not want any photo images on this design, illustrations and text only.

```html
<!DOCTYPE html>
<html lang="en">
<head>
<meta charset="utf-8">
<title>Gumridge Meats – Beef Jerky Pack</title>
<link href="https://fonts.googleapis.com/css2?family=Bebas+Neue&family=Oswald:wght@400;500;600&family=Rye&family=Alfa+Slab+One&family=Rokkitt:wght@700&family=Roboto+Condensed:wght@400;700&display=swap" rel="stylesheet">
<style>
  :root{
    --ink:#1b1b1b;
    --black:#111;
    --yellow:#f6c512;
    --grey:#cfcfd1;
    --grey-light:#ececed;
    --white:#fff;
    --guide:#e0409a;
  }
  *{box-sizing:border-box;margin:0;padding:0}
  html,body{width:1200px;height:929px;overflow:hidden;background:var(--white)}
  .pack{position:relative;width:1200px;height:929px;background:var(--ink);overflow:hidden;font-family:"Roboto Condensed",sans-serif;color:var(--white)}
  .abs{position:absolute}
  .center{text-align:center}

  /* front */
  .front-claim{left:0;width:600px;top:30px;font-family:"Rye",serif;font-size:25px;color:var(--yellow);text-align:center;letter-spacing:.5px}
  .scene{left:0;top:96px;width:600px;height:354px;
    background:
      radial-gradient(ellipse 230px 210px at 300px 190px,#e2e2e3 0%,#d6d6d7 70%,rgba(214,214,215,0) 100%),
      linear-gradient(180deg,#f4f4f5 0%,#e6e6e7 30%,#bdbdbf 70%,#8d8d90 92%,#2a2a2a 100%)}
  .brand-name{font-family:"Bebas Neue",sans-serif;color:var(--white);line-height:1;text-align:center}
  .front-brand{left:0;width:600px;top:484px;font-size:80px;letter-spacing:1px}
  .front-brand-sub{left:0;width:600px;top:562px;font-size:48px}
  .product{left:200px;width:204px;top:656px;height:54px;border-top:3px solid var(--yellow);border-bottom:3px solid var(--yellow);font-family:"Oswald",sans-serif;font-weight:600;font-size:40px;line-height:46px;letter-spacing:2px;text-align:center}
  .stars{left:0;width:600px;top:712px;color:var(--yellow);font-size:13px;letter-spacing:5px;text-align:center}
  .flavour{left:0;width:600px;top:748px;font-family:"Alfa Slab One",serif;font-size:24px;text-align:center;letter-spacing:.5px}
  .net{left:238px;top:804px;width:128px;height:125px;background:var(--yellow);border-radius:6px 6px 0 0;color:var(--black);font-family:"Rokkitt",serif;font-weight:700;font-size:21px;letter-spacing:4px;text-align:center;padding-top:6px;line-height:26px}
  .badge-box{left:78px;top:800px;width:66px;height:70px;border:3px solid var(--white);border-radius:4px}
  .badge-round{left:440px;top:798px;width:74px;height:74px;border:3px solid var(--white);border-radius:50%}

  /* back */
  .back-brand{left:600px;width:596px;top:226px;font-size:64px;letter-spacing:1px}
  .back-brand-sub{left:600px;width:596px;top:284px;font-size:38px}
  .rule{height:3px;background:var(--yellow)}
  .claims{font-family:"Oswald",sans-serif;font-size:10.5px;font-weight:400;letter-spacing:0;list-style:none}
  .claims li{position:absolute;white-space:nowrap}
  .claims li::before{content:"•";margin-right:6px}
  .seal{width:54px;height:54px;border-radius:50%;background:var(--white);border:3px solid var(--grey)}
  .heading{font-family:"Oswald",sans-serif;font-weight:500;font-size:17px;color:var(--yellow)}
  .body{font-size:12.5px;line-height:16px;color:#f0f0f0}
  .caps{font-family:"Oswald",sans-serif;font-size:15px;letter-spacing:1.5px}
  .maker b{font-family:"Oswald",sans-serif;font-weight:500;font-size:15px;letter-spacing:.3px}

  .facts{left:906px;top:533px;width:220px;height:255px;background:var(--white);border:3px solid #ddd;outline:2px solid var(--black);outline-offset:-6px;color:var(--black);padding:8px 9px}
  .facts h3{font-family:"Roboto Condensed",sans-serif;font-weight:700;font-size:29px;line-height:30px;letter-spacing:-.3px}
  .facts .small{font-size:9.5px;line-height:12px}
  .facts table{width:100%;border-collapse:collapse;font-size:9.5px;margin-top:4px}
  .facts td{padding:1.5px 2px;border-bottom:1px solid var(--black)}
  .facts td:nth-child(2){text-align:left;padding-left:18px}
  .facts td:last-child{text-align:right}
  .facts td:first-child{font-weight:700}
  .facts .thick{border-top:7px solid var(--black)}
  .facts .note{font-size:9px;line-height:11px;padding-top:3px}
  .facts .foot{font-size:7.5px;border-top:3px solid var(--black);margin-top:3px;padding-top:2px}
</style>
</head>
<body>
<div class="pack">

  <!-- front panel -->
  <div class="abs front-claim">HIGH IN PROTEIN ★ LOW IN FAT</div>
  <div class="abs scene" role="img" aria-label="Silhouettes of two riders on horseback before a pale setting sun in a rocky outback landscape with bush scrub"></div>

  <svg class="abs" style="left:0;top:0" width="1200" height="929" aria-hidden="true">
    <polygon points="0,565 178,684 0,805" fill="var(--yellow)"/>
    <polygon points="0,582 166,684 0,786" fill="var(--grey)"/>
    <polygon points="600,565 422,684 600,805" fill="var(--yellow)"/>
    <polygon points="600,582 434,684 600,786" fill="var(--grey)"/>
    <path d="M150 768 q20 -12 40 -5 q-17 -1 -29 8 z" fill="var(--yellow)"/>
    <path d="M450 768 q-20 -12 -40 -5 q17 -1 29 8 z" fill="var(--yellow)"/>
    <g stroke="var(--guide)" stroke-width="1" stroke-dasharray="4 3" fill="none">
      <line x1="30" y1="0" x2="30" y2="929"/>
      <line x1="570" y1="0" x2="570" y2="929"/>
      <line x1="600" y1="0" x2="600" y2="929"/>
      <line x1="628" y1="0" x2="628" y2="929"/>
      <line x1="1170" y1="0" x2="1170" y2="929"/>
      <line x1="0" y1="176" x2="1200" y2="176"/>
      <line x1="0" y1="210" x2="1200" y2="210"/>
      <rect x="3" y="3" width="1194" height="923"/>
    </g>
  </svg>

  <div class="abs brand-name front-brand">GUMRIDGE</div>
  <div class="abs brand-name front-brand-sub">MEATS</div>
  <div class="abs product">BEEF JERKY</div>
  <div class="abs stars">★★★</div>
  <div class="abs flavour">BLACK PAPPER</div>
  <div class="abs badge-box"></div>
  <div class="abs net">NET WT.<br>75g<br>★</div>
  <div class="abs badge-round"></div>

  <!-- back panel -->
  <div class="abs brand-name back-brand">GUMRIDGE</div>
  <div class="abs brand-name back-brand-sub">MEATS</div>

  <div class="abs rule" style="left:672px;top:360px;width:452px"></div>
  <ul class="abs claims" style="left:0;top:0">
    <li style="left:678px;top:370px">60 CALORIES</li>
    <li style="left:776px;top:370px">WHEAT FREE</li>
    <li style="left:678px;top:397px">LOW IN FAT</li>
    <li style="left:776px;top:397px">MINIMALLY PROCESSED</li>
    <li style="left:678px;top:424px">100% PURE ANGUS</li>
    <li style="left:776px;top:424px">NO ARTIFICIAL INGREDIENTS</li>
  </ul>
  <div class="abs seal" style="left:921px;top:374px"></div>
  <div class="abs seal" style="left:993px;top:374px"></div>
  <div class="abs seal" style="left:1065px;top:374px"></div>
  <div class="abs rule" style="left:672px;top:447px;width:452px"></div>

  <div class="abs heading" style="left:671px;top:468px">INGREDIENTS</div>
  <p class="abs body" style="left:671px;top:490px;width:455px">Australian beef, sugar, spices, salt, soy (water, soyabeans, salt, wheat flour, potassium sorbate (E202)), monosodium glutamate (E621).</p>
  <p class="abs body" style="left:671px;top:538px">Allergens Contains soy and wheat flour.</p>
  <p class="abs body" style="left:671px;top:570px;width:230px">Please store in a dry airtight container after opening and keep away from direct sunlight.</p>

  <div class="abs rule" style="left:672px;top:636px;width:220px;height:2px"></div>
  <div class="abs caps" style="left:672px;top:642px">REFRIGERATE AFTER OPENING</div>
  <div class="abs rule" style="left:672px;top:668px;width:220px;height:2px"></div>

  <div class="abs body maker" style="left:671px;top:677px">Manufactured for:<br><b>REDGULLY PTY LTD</b><br>18 Banksia Rd<br>Wattle Flat QLD 4075</div>

  <div class="abs rule" style="left:672px;top:755px;width:220px;height:2px"></div>
  <div class="abs caps center" style="left:672px;top:766px;width:220px;font-size:13px">AUSTRALIAN MADE AND OWNED</div>

  <div class="abs facts">
    <h3>Nutrition Facts</h3>
    <div class="small">Serving size 25g</div>
    <div class="small" style="text-align:right;margin-top:12px">Serving per packet&nbsp;&nbsp; Per serving Per 100g</div>
    <table>
      <tr><td colspan="3" class="thick" style="text-align:right;font-weight:700;padding-left:0">% Daily Value*</td></tr>
      <tr><td>Energy</td><td>405kJ</td><td>1215kJ</td></tr>
      <tr><td>Protein</td><td>12.6g</td><td>38.0g</td></tr>
      <tr><td>Fat</td><td>2.2g</td><td>6.7g</td></tr>
      <tr><td>Carbohydrates</td><td>6.3g</td><td>18.9g</td></tr>
      <tr><td>Sugar</td><td>5.9g</td><td>17.8g</td></tr>
      <tr><td>Sodium</td><td>276mg</td><td>830mg</td></tr>
    </table>
    <div class="note">Not a significant source of saturated fat, trans fat, dietary fiber and calcium.</div>
    <div class="foot">* Percent Daily Values are based on a 2,000 Calorie diet.</div>
  </div>

</div>
</body>
</html>
```